GearLoom is a company based in dubai that acts as a market place for the automotive industry

from a b2c prospective our company acts as a marketplace that offers :

*booking services for car workshops whereas users can find nearest car workshop and book desired services.
* review, rate, the workshop once service i complete.
*pickup and drop off services (offered from the workshop).
*inspection services (offered from the workshop).
_______________________________________

*users can display or view a car to sell or buy.

*online merchant store for (parts, accessories, gadgets).
________________________________________

- a live customer service feature in the website.
- signing up options.

Target Market(s)

three target segments:
- customers that need to fix their cars.
- car workshop owners
-merchants
-people that want to buy/sell their car

Industry/Entity Type

Automotive

Contact Information for Business Card

frontside: name, email, landline number, mobile number, location, social media
back side: only logo

Logo Text

Gearloom

Number of Pages Required

3 page

Font styles to use
Other font styles liked:
• Dubai font

```html
<!DOCTYPE html>
<html lang="en">
<head>
<meta charset="utf-8">
<title>GearLoom – Automotive Marketplace</title>
<link rel="stylesheet" href="https://fonts.googleapis.com/css2?family=Nunito:ital,wght@0,400;0,600;0,800;1,400&display=swap">
<style>
:root{
  --ink:#333333;
  --ink-soft:#555555;
  --card:#333333;
  --white:#ffffff;
  --band:#f1f1f1;
  --line:#e4e4e4;
  --social:#1e5aa0;
  --hero-a:#c9ccd1;
  --hero-b:#7d8796;
  --hero-c:#2f3f66;
}
*{box-sizing:border-box;margin:0;padding:0}
html,body{width:818px;height:1200px;overflow:hidden;background:var(--white)}
body{font-family:"Nunito",sans-serif;color:var(--ink);position:relative}

.site-header{height:78px;position:relative}
.brand{position:absolute;left:90px;top:25px;display:flex;align-items:center;gap:7px;
  font-weight:800;font-size:25px;letter-spacing:.5px;text-transform:uppercase;color:#111}
.brand-dot{width:20px;height:20px;border-radius:50%;background:#111}
.main-nav{position:absolute;right:90px;top:33px;display:flex;gap:26px;font-size:10.5px}
.main-nav a{color:var(--ink);text-decoration:none;padding-bottom:3px}
.main-nav a.active{border-bottom:1px solid var(--ink)}

.hero{position:absolute;top:78px;left:0;width:818px;height:341px;
  background:linear-gradient(100deg,var(--hero-a) 0%,#e3e5e8 35%,var(--hero-b) 62%,var(--hero-c) 75%,#b9bec6 100%)}
.hero-arrow{position:absolute;top:160px;width:16px;height:21px;background:#222;display:flex;align-items:center;justify-content:center}
.hero-arrow.prev{left:0}.hero-arrow.next{right:0}
.hero-caption{position:absolute;left:191px;top:280px;width:437px;height:41px;background:rgba(30,30,30,.88);
  color:var(--white);font-size:19px;display:flex;align-items:center;justify-content:center}

.services{position:absolute;top:455px;left:0;width:818px}
.section-title{text-align:center;font-weight:400;font-size:30px;color:var(--ink)}
.service-grid{position:absolute;top:57px;left:90px;width:638px;display:grid;
  grid-template-columns:repeat(3,203px);column-gap:14.5px;row-gap:17px}
.service-card{height:130px;overflow:hidden;background:var(--card);color:var(--white);
  padding:18px 8px 0 12px;font-size:10.7px;letter-spacing:-0.1px;line-height:17.6px}
.service-card svg{display:block;height:30px;margin-bottom:10px}

.reviews{position:absolute;top:838px;left:0;width:818px;height:282px;background:var(--band)}
.reviews .section-title{margin-top:47px;font-size:29px}
.review-quote{width:640px;margin:7px auto 0;text-align:center;font-style:italic;font-size:11.4px;line-height:17.6px;color:var(--ink-soft)}
.review-author{text-align:center;font-size:11.4px;margin-top:6px;color:#222}
.review-avatar{position:absolute;left:382px;top:173px;width:54px;height:54px;border-radius:50%;
  background:radial-gradient(circle at 50% 40%,#d9b9a1 0%,#b89a86 45%,#9a9a9a 100%);border:2px solid #ddd}
.review-arrow{position:absolute;top:124px}
.review-arrow.prev{left:27px}.review-arrow.next{right:27px}

.site-footer{position:absolute;top:1120px;left:0;width:818px;height:80px}
.footer-links{position:absolute;left:90px;top:25px;font-size:8.5px;color:var(--ink)}
.footer-links span{margin:0 6px}
.copyright{position:absolute;left:90px;top:45px;font-size:8.5px;color:var(--ink-soft)}
.social{position:absolute;left:665px;top:31px;display:flex;gap:4px}
.social i{width:18px;height:18px;border-radius:50%;background:var(--social);display:block}
</style>
</head>
<body>
<header class="site-header">
  <div class="brand"><span class="brand-dot"></span>Gearloom</div>
  <nav class="main-nav">
    <a class="active" href="#">Home</a><a href="#">About Us</a><a href="#">Services</a><a href="#">Reviews</a><a href="#">Contact Us</a>
  </nav>
</header>

<section class="hero" role="img" aria-label="Mechanic in a blue uniform working under a car raised on a lift in a workshop">
  <div class="hero-arrow prev"><svg width="8" height="14" viewBox="0 0 8 14"><path d="M7 1 1 7l6 6" fill="none" stroke="#fff" stroke-width="1"/></svg></div>
  <div class="hero-arrow next"><svg width="8" height="14" viewBox="0 0 8 14"><path d="M1 1l6 6-6 6" fill="none" stroke="#fff" stroke-width="1"/></svg></div>
  <div class="hero-caption">Phasellus nisl est, condimentum vitae faucibus</div>
</section>

<section class="services">
  <h2 class="section-title">Our Services</h2>
  <div class="service-grid">
    <div class="service-card">
      <svg viewBox="0 0 20 30" width="20"><path d="M10 1a9 9 0 0 0-9 9c0 7 9 19 9 19s9-12 9-19a9 9 0 0 0-9-9z" fill="#fff"/><circle cx="10" cy="10" r="3.5" fill="#333"/></svg>
      Booking services for car workshops whereas users can find nearest car workshop and book desired services.
    </div>
    <div class="service-card">
      <svg viewBox="0 0 32 30" width="32"><path d="M16 1l4.6 9.6 10.4 1.3-7.6 7.2 2 10.4L16 24.4 6.6 29.5l2-10.4L1 11.9l10.4-1.3z" fill="#fff"/></svg>
      Review, rate, the workshop once service i complete
    </div>
    <div class="service-card">
      <svg viewBox="0 0 38 30" width="38"><path d="M8 3h22l5 10v13h-6v-4H9v4H3V13z" fill="#fff"/><path d="M10 6h18l3 7H7z" fill="#333"/><circle cx="10" cy="17" r="2.5" fill="#333"/><circle cx="28" cy="17" r="2.5" fill="#333"/></svg>
      Pickup and drop off services (offered from the workshop)
    </div>
    <div class="service-card">
      <svg viewBox="0 0 32 30" width="32"><rect x="2" y="5" width="23" height="23" rx="4" fill="none" stroke="#fff" stroke-width="3"/><path d="M8 15l6 6L30 4" fill="none" stroke="#fff" stroke-width="4"/></svg>
      Inspection services (offered from the workshop)
    </div>
    <div class="service-card">
      <svg viewBox="0 0 30 30" width="30"><path d="M2 2h12l14 14-12 12L2 14z" fill="#fff"/><circle cx="8" cy="8" r="2.5" fill="#333"/></svg>
      Users can display or view a car to sell or buy.
    </div>
    <div class="service-card">
      <svg viewBox="0 0 34 30" width="34"><path d="M1 3h6l4 16h18l3-12H9" fill="none" stroke="#fff" stroke-width="3"/><path d="M9 7h23l-3 12H11z" fill="#fff"/><circle cx="13" cy="26" r="2.5" fill="#fff"/><circle cx="27" cy="26" r="2.5" fill="#fff"/></svg>
      Online merchant store for (parts, accessories, gadgets).
    </div>
  </div>
</section>

<section class="reviews">
  <h2 class="section-title">Reviews</h2>
  <p class="review-quote">“ Phasellus blandit quam a ipsum gravida dapibus. Cras sed augue tortor. Suspendisse elit ligula, iaculis dignissim justo eu, vestibu lum venenatis elit. Sed egestas, nisl id cursus ultricies, turpis orci rhoncus odio, id tristique odio ex in lacus. Nam suscipit sapien eget blandit sollicitudin. Praesent elementum nulla sit amet justo.&nbsp; ”</p>
  <p class="review-author">- Sam Rivera, City name</p>
  <div class="review-avatar" role="img" aria-label="Portrait photo of the reviewer"></div>
  <svg class="review-arrow prev" width="10" height="16" viewBox="0 0 10 16"><path d="M9 1 2 8l7 7" fill="none" stroke="#999" stroke-width="1.5"/></svg>
  <svg class="review-arrow next" width="10" height="16" viewBox="0 0 10 16"><path d="M1 1l7 7-7 7" fill="none" stroke="#999" stroke-width="1.5"/></svg>
</section>

<footer class="site-footer">
  <div class="footer-links">Home<span>|</span>About Us<span>|</span>Services<span>|</span>Reviews<span>|</span>Contact Us</div>
  <div class="copyright">Copyright ©&nbsp; 2017&nbsp;&nbsp; GearLoom.&nbsp;&nbsp; All rights reserved.</div>
  <div class="social" aria-label="Social media links"><i></i><i></i><i></i></div>
</footer>
</body>
</html>
```